Kid's Cancer Camp Business Card

Create a unique Two-Sided color business cards for Camp Willow Brook, a pediatric cancer camp.

The camp tag line is: a place where every camper finds the sun...

Dale Morrisey, Executive Director
Camp Willow Brook Charitable Foundation, Inc
PO Box 918
Alder Falls, VT 06832

Phone - 203-555-0143
Fax - 203-555-0187
Email: dale@campwillowbrook.example
www.campwillowbrook.example

Target Market(s)

Potential Donors, Volunteers and Campers

Industry/Entity Type

Non-profit pediatric cancer camp

Contact Information for Business Card

All contact info that is included in the description

Font styles to use
Other font styles liked:
• Designer chooses font

Requirements
Must have
• Camp Willow Brook Logo and Tag Line
Nice to have
• should be eye catching
Should not have
• not cartoony

```html
<!DOCTYPE html>
<html lang="en">
<head>
<meta charset="utf-8">
<title>Camp Willow Brook – Business Card</title>
<link rel="stylesheet" href="https://fonts.googleapis.com/css2?family=Lato:wght@400;700;900&family=Delius&display=swap">
<style>
  :root {
    --backdrop: #1f1f1f;
    --camp-blue: #1173b2;
    --ink-blue: #1669a8;
    --sun-gold: #fbb92d;
    --accent-orange: #f6a623;
    --teal: #18a3a0;
    --card-white: #ffffff;
    --text-dark: #333333;
  }
  * { box-sizing: border-box; margin: 0; padding: 0; }
  html, body {
    width: 1200px; height: 939px; overflow: hidden;
    background: var(--backdrop);
    font-family: "Lato", sans-serif;
  }
  .canvas { position: relative; width: 1200px; height: 939px; }

  .card {
    position: absolute; width: 600px; height: 340px; border-radius: 22px;
  }

  /* Front */
  .card-front {
    left: 140px; top: 100px; background: var(--camp-blue); color: var(--card-white);
    display: flex; flex-direction: column; align-items: center; justify-content: center;
  }
  .front-mark { display: flex; flex-direction: column; align-items: center; gap: 18px; margin-top: -10px; }
  .front-mark .mark-circle { width: 110px; height: 110px; border-radius: 50%; background: var(--card-white); }
  .front-mark .brand-name { font-size: 38px; font-weight: 400; letter-spacing: 0.5px; }
  .tagline {
    position: absolute; bottom: 34px; width: 100%; text-align: center;
    font-family: "Delius", cursive; font-size: 19px; letter-spacing: 0.3px;
  }

  /* Back */
  .card-back {
    left: 460px; top: 490px; background: var(--card-white);
    display: flex; align-items: center; padding: 0 30px 0 34px;
  }
  .back-mark { width: 230px; display: flex; flex-direction: column; align-items: center; gap: 16px; }
  .back-mark .mark-circle { width: 96px; height: 96px; border-radius: 50%; background: var(--sun-gold); }
  .back-mark .brand-name { font-size: 27px; font-weight: 400; color: var(--ink-blue); white-space: nowrap; }
  .divider { width: 2px; height: 250px; background: var(--teal); margin: 0 26px 0 20px; }

  .contact { flex: 1; color: var(--text-dark); }
  .person-name { font-size: 34px; font-weight: 900; color: var(--ink-blue); line-height: 1; }
  .person-title { font-size: 18px; color: var(--accent-orange); margin: 4px 0 14px; }
  .contact-row { display: flex; align-items: flex-start; gap: 10px; margin-bottom: 5px; }
  .contact-row svg { flex: none; width: 14px; height: 14px; margin-top: 3px; fill: var(--ink-blue); }
  .contact-row .value { font-size: 14px; line-height: 1.35; white-space: nowrap; }
  .contact-row .value.large { font-size: 19px; line-height: 1.15; }
  .contact-row.address .value { font-weight: 400; font-size: 14.5px; }
</style>
</head>
<body>
<main class="canvas">

  <section class="card card-front" aria-label="Card front">
    <div class="front-mark">
      <span class="mark-circle"></span>
      <span class="brand-name">camp willow brook</span>
    </div>
    <p class="tagline">a place where every camper finds the sun...</p>
  </section>

  <section class="card card-back" aria-label="Card back">
    <div class="back-mark">
      <span class="mark-circle"></span>
      <span class="brand-name">camp willow brook</span>
    </div>

    <span class="divider"></span>

    <div class="contact">
      <h1 class="person-name">Dale Morrisey</h1>
      <p class="person-title">Executive Director</p>

      <div class="contact-row address">
        <svg viewBox="0 0 24 24" aria-hidden="true"><path d="M12 2a7 7 0 0 0-7 7c0 5 7 13 7 13s7-8 7-13a7 7 0 0 0-7-7zm0 9.5A2.5 2.5 0 1 1 12 6.5a2.5 2.5 0 0 1 0 5z"/></svg>
        <p class="value">Camp Willow Brook<br>Charitable Foundation, Inc<br>PO Box 918, Alder Falls, VT 06832</p>
      </div>
      <div class="contact-row">
        <svg viewBox="0 0 24 24" aria-hidden="true"><path d="M6.6 10.8a15.1 15.1 0 0 0 6.6 6.6l2.2-2.2a1 1 0 0 1 1-.25 11.4 11.4 0 0 0 3.6.57 1 1 0 0 1 1 1V20a1 1 0 0 1-1 1A17 17 0 0 1 3 4a1 1 0 0 1 1-1h3.5a1 1 0 0 1 1 1c0 1.250.2 2.45.57 3.57a1 1 0 0 1-.25 1z"/></svg>
        <p class="value large">203-555-0143</p>
      </div>
      <div class="contact-row">
        <svg viewBox="0 0 24 24" aria-hidden="true"><path d="M7 3h10v5H7zM4 9h16a2 2 0 0 1 2 2v6h-4v4H6v-4H2v-6a2 2 0 0 1 2-2zm4 7v3h8v-3z"/></svg>
        <p class="value large">203-555-0187</p>
      </div>
      <div class="contact-row">
        <svg viewBox="0 0 24 24" aria-hidden="true"><path d="M2 5h20v14H2zm2 2v.5l8 5 8-5V7z"/></svg>
        <p class="value">dale@campwillowbrook.example</p>
      </div>
      <div class="contact-row">
        <svg viewBox="0 0 24 24" aria-hidden="true"><path d="M12 2a10 10 0 1 0 0 20 10 10 0 0 0 0-20zm6.9 6h-3a15 15 0 0 0-1.3-3.9A8 8 0 0 1 18.9 8zM12 4c.9 1.2 1.6 2.5 2 4h-4c.4-1.5 1.1-2.8 2-4zM4.3 14a8 8 0 0 1 0-4h3.4a16 16 0 0 0 0 4zm.8 2h3a15 15 0 0 0 1.3 3.9A8 8 0 0 1 5.1 16zm3-8h-3a8 8 0 0 1 4.3-3.9A15 15 0 0 0 8.1 8zM12 20c-.9-1.2-1.6-2.5-2-4h4c-.4 1.5-1.1 2.8-2 4zm2.3-6H9.7a14 14 0 0 1 0-4h4.6a14 14 0 0 1 0 4zm.3 5.9a15 15 0 0 0 1.3-3.9h3a8 8 0 0 1-4.3 3.9zm1.7-5.9a16 16 0 0 0 0-4h3.4a8 8 0 0 1 0 4z"/></svg>
        <p class="value">www.campwillowbrook.example</p>
      </div>
    </div>
  </section>

</main>
</body>
</html>
```